Webdesign für Schnaps-Experten
Super gelaufen! Sorry für die Verzögerungen meinerseits, war so nicht geplant :-)
Zielgruppe
Es geht hier um ein Design für die Domain 'brandkundler.de'
Mit dieser will ich mich zunächst als Experte für Schnäpse aus dem deutschsprachigen Raum, Fokus auf Bayern positionieren. Später wird dann angestrebt, auch definierte zusammengestellte Schnapsprobierpakete zu verkaufen. Zielgruppe ist also der Personenkreis der gerne mal hochwertige Schnäpse geniesst und sich da zu Hintergründen informieren will
Ergänzung: Ich will später Tastings und Abo-Pakete anbieten (Whisky-Beispiel hier: https://www.morningpost-example.co.uk/extras/topchoice/food-drink/spirits/best-whiskey-subscription-k4921305.html), also eine virtuelle Reise mit Schnäpsen
Aufgabenstellung
Es gibt eine erste Logovorlage, mit dieser bitte planen, ansonsten gerne kreativ
Tendenziell viele Fotos

```html
<!DOCTYPE html>
<html lang="de">
<head>
<meta charset="utf-8">
<title>BRANDKUNDLER – Schnaps-Experte</title>
<link rel="stylesheet" href="https://fonts.googleapis.com/css2?family=Roboto:wght@400;500;700;900&display=swap">
<style>
:root{
  --bg:#12181b;
  --text:#ffffff;
  --muted:#c9cfd2;
  --card-text:#8a8f93;
  --accent:#f6b700;
  --card:#ffffff;
  --ink:#1a1d20;
  --line:#2a3236;
}
*{box-sizing:border-box;margin:0;padding:0}
html,body{width:1200px;height:3174px;overflow:hidden;background:var(--bg)}
body{position:relative;font-family:"Roboto",Arial,sans-serif;color:var(--text)}
.abs{position:absolute}
.brand{left:25px;top:38px;display:flex;align-items:center;gap:8px;font-size:12px;font-weight:500;letter-spacing:.5px}
.brand-mark{width:14px;height:14px;border-radius:50%;border:2px solid var(--text)}
.nav{top:55px;right:53px;display:flex;gap:19px;font-size:10.5px}
.side-dot{right:1px;top:152px;width:7px;height:7px;border-radius:50%;background:var(--accent)}
.scroll{left:1160px;top:306px;font-size:6px;writing-mode:vertical-rl;transform:rotate(180deg);color:var(--muted)}
.scroll-line{left:1167px;top:336px;width:1px;height:38px;background:#555}
.scroll-dot{left:1165px;top:332px;width:5px;height:5px;border-radius:50%;background:#fff}
.edit{left:1151px;top:625px;width:34px;height:34px;border-radius:50%;background:#1b2428;display:flex;align-items:center;justify-content:center}
.hero-title{left:0;width:1200px;top:106px;text-align:center;font-size:49px;line-height:56px;font-weight:400;z-index:2}
.photo{display:block}
.hero-photo{left:250px;top:163px;width:700px;height:362px;background:radial-gradient(ellipse at 50% 60%,#2f3a4c 0,#3b2518 40%,#1a0f0a 100%)}
.pill{display:inline-block;background:var(--accent);color:var(--ink);font-size:6.5px;font-weight:700;letter-spacing:.6px;padding:4px 9px;border-radius:10px}
.about-pill{left:250px;top:619px}
.h2{font-size:40px;font-weight:400}
.about-h{left:250px;top:638px}
.body-s{font-size:9.6px;line-height:12.5px;color:var(--muted)}
.col1{left:357px;top:718px;width:228px}
.col2{left:713px;top:718px;width:240px}
.man-photo{left:357px;top:785px;width:593px;height:283px;background:linear-gradient(90deg,#c89a55 0,#8d5a2b 45%,#3a2415 70%,#121212 100%)}
.pear-photo{left:250px;top:1002px;width:380px;height:253px;background:linear-gradient(180deg,#8fa56b 0,#b4b07a 40%,#6e5b3d 75%,#4a3b28 100%)}
.about-more{left:732px;top:1103px;width:215px}
.big15{left:733px;top:1140px;font-size:88px;font-weight:700;line-height:100px}
.years{left:855px;top:1190px;font-size:12px;line-height:20px;font-weight:500}
.btn{display:flex;align-items:center;justify-content:center;background:var(--accent);color:var(--ink);font-size:10.5px;height:25px}
.about-btn{left:732px;top:1248px;width:96px}
.blog-h{left:250px;top:1362px}
.filters{top:1431px;font-size:8.6px}
.filters.on{color:var(--accent)}
.card{background:var(--card);color:var(--ink)}
.card-img{height:126px;position:relative;background:linear-gradient(180deg,#06080d 0,#0b1424 55%,#26303a 75%,#05070a 100%)}
.card-img.still{background:linear-gradient(90deg,#5a3a22,#b8865a 30%,#8a8f94 55%,#c99b6a 80%,#4a2d19)}
.card-img.bottles{background:linear-gradient(90deg,#3a2a1a,#c8a060 20%,#b83a2a 40%,#d8b070 60%,#a33a2a 80%,#3a2a1a)}
.tag{position:absolute;left:16px;top:16px;background:#1e2326;color:#fff;font-size:6px;font-weight:700;letter-spacing:.6px;padding:3px 7px;border-radius:8px}
.card-body{padding:16px 20px 0 20px}
.meta{font-size:7.8px;color:#777;display:flex;gap:10px}
.meta b{font-weight:500;color:var(--ink)}
.card h3{font-size:11px;font-weight:700;margin:8px 0 8px}
.card p{font-size:9px;line-height:16px;color:var(--card-text)}
.tile{overflow:hidden}
.tile-dark{background:linear-gradient(90deg,#000 0,#03050a 55%,#0c1a33 75%,#020306 100%)}
.tile-trip{background:linear-gradient(180deg,#8d6b4a 0,#a57c55 55%,#2b2a2e 80%,#7a1e24 100%)}
.tile-cap{position:absolute;left:20px;bottom:22px}
.chip{display:inline-block;font-size:6.5px;padding:3px 5px;background:#fff;color:var(--ink)}
.chip.dark{background:#3a3f43;color:#fff}
.tile-title{font-weight:900;color:#fff;margin-top:6px}
.tile-big .tile-title{font-size:22px}
.tile-small .tile-title{font-size:14px}
.posted{font-size:7px;color:#aaa;margin-top:6px}
.footer-line{left:0;top:3114px;width:1200px;height:1px;background:var(--line)}
.footer-txt{left:250px;top:3137px;font-size:8.6px}
.footer-txt u{color:#fff}
.social{top:3136px;width:11px;height:11px;border:1.5px solid #fff;border-radius:2px}
</style>
</head>
<body>

<header>
  <div class="abs brand"><span class="brand-mark"></span>BRANDKUNDLER</div>
  <nav class="abs nav"><span>Startseite</span><span>Über mich</span><span>Blog</span><span>Kontakt</span></nav>
</header>

<div class="abs side-dot"></div>
<div class="abs scroll">scroll</div>
<div class="abs scroll-line"></div>
<div class="abs scroll-dot"></div>
<div class="abs edit">
  <svg width="13" height="13" viewBox="0 0 13 13" fill="none" stroke="#fff" stroke-width="1.3"><path d="M2 11l1-3 6-6 2 2-6 6z"/></svg>
</div>

<section class="hero">
  <h1 class="abs hero-title">Herzlich Willkommen bei den<br>BRANDKUNDLER</h1>
  <div class="abs photo hero-photo" role="img" aria-label="Foto: Schnapsexperte im Anzug vor einer Bar mit Flaschenregal"></div>
</section>

<section class="about">
  <span class="abs pill about-pill">ÜBER MICH</span>
  <h2 class="abs h2 about-h">Max Mustermann</h2>
  <p class="abs body-s col1">Muster Text Lorem ipsum dolor sit amet, consetetur sadipscing elitr, sed diam nonumy eirmod tempor est invidunt ut labore et dolore magna aliquyam erat sed diam voluptua.</p>
  <p class="abs body-s col2">Et vero eos et accusam et justo duo dolores etea rebum. Stet clita kasd gubergren, no sea takimata sanctus est Lorem ipsum dolor sit amet. Lorem ipsum dolor sit amet consetetur sadipscing elitr.</p>
  <div class="abs photo man-photo" role="img" aria-label="Foto: Mann im Hemd mit Krawatte vor unscharfem Hintergrund mit Glas"></div>
  <div class="abs photo pear-photo" role="img" aria-label="Foto: Birnen im Korb mit Karaffe und Schnapsgläsern auf Holztisch"></div>
  <p class="abs body-s about-more">Stet clita kasd gubergren, no sea takimata sanctus est Lorem ipsum dolor sit amet. Lorem ipsum dolor sit amet, consetetur sadipscing elitr...</p>
  <div class="abs big15">15</div>
  <div class="abs years">Jahre<br>Expertise</div>
  <div class="abs btn about-btn">Mehr erfahren</div>
</section>

<section class="blog">
  <h2 class="abs h2 blog-h">Blog</h2>
  <span class="abs filters on" style="left:286px">All</span>
  <span class="abs filters" style="left:318px">Allgemein</span>
  <span class="abs filters" style="left:377px">Anbietern</span>
  <span class="abs filters" style="left:436px">Schnäpse</span>
  <span class="abs filters" style="left:495px">Schnapsreisen</span>
  <span class="abs filters" style="left:574px">Werkzeuge</span>

  <article class="abs card" style="left:250px;top:1476px;width:221px;height:272px">
    <div class="card-img still" role="img" aria-label="Foto: kupferne Brennanlage"><span class="tag">WERKZEUGE</span></div>
    <div class="card-body"><div class="meta"><b>admin</b><span>•</span><span>2 Stunden ago</span></div>
      <h3>Muster Werkzeug Name</h3>
      <p>Muster Text Lorem ipsum dolor sit amet sed diam nonumy eirmod tempor vero eos sed diam voluptua. At vero eos et accusam et justo duo dolores et ea rebum. Stet clita kasd gubergren, no sea takimata sanctus...</p></div>
  </article>
  <article class="abs card" style="left:489px;top:1476px;width:221px;height:272px">
    <div class="card-img" role="img" aria-label="Foto: blaue Wodkaflasche im Wasserspritzer"><span class="tag">ANBIETERN</span></div>
    <div class="card-body"><div class="meta"><b>admin</b><span>•</span><span>2 Stunden ago</span></div>
      <h3>Muster Anbieter Name</h3>
      <p>Muster Text Lorem ipsum dolor sit amet sed diam nonumy eirmod tempor vero eos et accusam et justo duo dolores et ea rebum. Stet clita kasd gubergren, no sea takimata sanctus est Lorem ipsum...</p></div>
  </article>
  <article class="abs card" style="left:728px;top:1476px;width:221px;height:257px">
    <div class="card-img" role="img" aria-label="Foto: blaue Wodkaflasche im Wasserspritzer"><span class="tag">ANBIETERN</span></div>
    <div class="card-body"><div class="meta"><b>admin</b><span>•</span><span>2 Stunden ago</span></div>
      <h3>Muster Anbieter Name</h3>
      <p>Muster Text Lorem vero eos et accusam et justo duo dolores et ea rebum. Stet clita kasd gubergren, no sea ipsum dolor sit amet sed diam nonumy eirmod tempor...</p></div>
  </article>
  <article class="abs card" style="left:250px;top:1768px;width:221px;height:272px">
    <div class="card-img" role="img" aria-label="Foto: blaue Wodkaflasche im Wasserspritzer"><span class="tag">ANBIETERN</span></div>
    <div class="card-body"><div class="meta"><b>admin</b><span>•</span><span>3 Stunden ago</span></div>
      <h3>Muster Anbieter Name</h3>
      <p>Muster Text Lorem ipsum dolor sit amet sed diam nonumy eirmod tempor vero eos et accusam et justo duo dolores et ea rebum. Stet clita kasd gubergren, no sea takimata sanctus est Lorem ipsum fedil...</p></div>
  </article>
  <article class="abs card" style="left:489px;top:1768px;width:221px;height:256px">
    <div class="card-img bottles" role="img" aria-label="Foto: drei Schnapsflaschen mit Etiketten"><span class="tag">SCHNÄPSE</span></div>
    <div class="card-body"><div class="meta"><b>admin</b><span>•</span><span>6 Stunden ago</span></div>
      <h3>Muster Schnaps Name</h3>
      <p>Muster text consetetur sadipscing elitr, sed diam nonumy eirmod tempor invidunt ut labore et dolore magna aliquyam erat, sed diam voluptua...</p></div>
  </article>
  <article class="abs card" style="left:728px;top:1752px;width:221px;height:224px">
    <div class="card-img" role="img" aria-label="Foto: blaue Wodkaflasche im Wasserspritzer"><span class="tag">ANBIETERN</span></div>
    <div class="card-body"><div class="meta"><b>admin</b><span>•</span><span>2 Stunden ago</span></div>
      <h3>Muster Anbieter Name</h3>
      <p>Muster Text Lorem ipsum dolor sit amet sed diam nonumy...</p></div>
  </article>

  <div class="abs btn" style="left:549px;top:2060px;width:100px">Ältere Beiträge</div>
</section>

<section class="distillers">
  <h2 class="abs h2" style="left:250px;top:2173px">Schnapsbrennern</h2>
  <div class="abs tile tile-dark tile-big" style="left:250px;top:2241px;width:460px;height:276px" role="img" aria-label="Foto: Wodkaflasche im Wasserspritzer vor schwarzem Grund">
    <div class="tile-cap"><span class="chip">2 Stunden ago</span><span class="chip dark">Anbietern</span>
      <div class="tile-title">Muster Anbieter Name</div><div class="posted">Posted by admin</div></div>
  </div>
  <div class="abs tile tile-dark tile-small" style="left:728px;top:2241px;width:221px;height:132px" role="img" aria-label="Foto: Wodkaflasche im Wasserspritzer">
    <div class="tile-cap"><span class="chip dark">Anbietern</span><div class="tile-title">Muster Anbieter Name</div></div>
  </div>
  <div class="abs tile tile-dark tile-small" style="left:728px;top:2393px;width:221px;height:131px" role="img" aria-label="Foto: Wodkaflasche im Wasserspritzer">
    <div class="tile-cap"><span class="chip dark">Anbietern</span><div class="tile-title">Muster Anbieter Name</div></div>
  </div>
  <div class="abs btn" style="left:524px;top:2544px;width:152px">Weitere Schnapsbrennern</div>
</section>

<section class="trips">
  <h2 class="abs h2" style="left:250px;top:2658px">Schnapsreisen</h2>
  <div class="abs tile tile-trip tile-big" style="left:250px;top:2725px;width:460px;height:276px" role="img" aria-label="Foto: Verkostungskarton mit Probierfläschchen">
    <div class="tile-cap"><span class="chip">41 Minuten ago</span><span class="chip dark">Schnapsreisen</span>
      <div class="tile-title">Muster Schnapsreise</div><div class="posted">Posted by admin</div></div>
  </div>
  <div class="abs tile tile-trip tile-small" style="left:728px;top:2725px;width:221px;height:133px" role="img" aria-label="Foto: Verkostungskarton mit Probierfläschchen">
    <div class="tile-cap"><span class="chip dark">Schnapsreisen</span><div class="tile-title">Muster Schnapsreise</div></div>
  </div>
  <div class="abs tile tile-trip tile-small" style="left:728px;top:2877px;width:221px;height:132px" role="img" aria-label="Foto: Verkostungskarton mit Probierfläschchen">
    <div class="tile-cap"><span class="chip dark">Schnapsreisen</span><div class="tile-title">Muster Schnapsreise</div></div>
  </div>
  <div class="abs btn" style="left:572px;top:3028px;width:55px">Shop</div>
</section>

<footer>
  <div class="abs footer-line"></div>
  <p class="abs footer-txt">© 2022 BRANDKUNDLER. Alle Rechte vorbehalten. <u>Impressum</u> / <u>Datenschutz</u></p>
  <span class="abs social" style="left:876px" aria-label="Social-Media-Link"></span>
  <span class="abs social" style="left:905px" aria-label="Social-Media-Link"></span>
  <span class="abs social" style="left:935px" aria-label="Social-Media-Link"></span>
</footer>

</body>
</html>
```